Sunny Paths and joy Business card

I have a logo, but will like a business card design. Is for a travel agency in Mexico. We focus in family experiences.

I will liek some thing different and unique, from the traditional business card, something to get remmeber for.

Business card information:

Leandro T. Ocampo
leandro@sunnypathsjoy.example

Alameda 482, 3 piso
Col. Tlalpizco
Mexico, D.F. 07320

office: (55) 5000-0142
mobile: (55) 9000-0187

www.sunnypathsjoy.example
@sunnypjoy
blog: sunnypathsandjoy.blogsite.example
facebook: SunnyPathsAndJoy

```html
<!DOCTYPE html>
<html lang="es">
<head>
<meta charset="utf-8">
<title>Sunny Paths and joy — Business card</title>
<link rel="stylesheet" href="https://fonts.googleapis.com/css2?family=Poppins:ital,wght@1,400&family=Roboto+Condensed:ital,wght@1,400&display=swap">
<style>
  :root {
    --sky-top: #6f9ff7;
    --sky-mid: #3a72ef;
    --sea-top: #1448dc;
    --sea-bottom: #0a2a98;
    --frame: rgba(160, 200, 255, 0.55);
    --brand-orange: #f28a3a;
    --brand-outline: #3b2210;
    --name-blue: #9cc2ff;
    --text-white: #ffffff;
    --ribbon-tint: rgba(200, 220, 255, 0.22);
    --ribbon-fade: rgba(200, 220, 255, 0);
  }
  html, body {
    margin: 0;
    padding: 0;
    width: 1200px;
    height: 900px;
    overflow: hidden;
    background: #ffffff;
  }
  .card {
    position: relative;
    width: 1200px;
    height: 900px;
    overflow: hidden;
    background:
      linear-gradient(to bottom,
        var(--sky-top) 0%,
        var(--sky-mid) 44.4%,
        var(--sea-top) 44.5%,
        var(--sea-bottom) 100%);
    font-family: "Roboto Condensed", "Arial Narrow", sans-serif;
    font-style: italic;
    color: var(--text-white);
  }
  .card__frame {
    position: absolute;
    inset: 10px;
    border: 6px solid var(--frame);
    pointer-events: none;
  }
  .path-ribbon {
    position: absolute;
    left: 450px;
    top: 190px;
    width: 440px;
    height: 600px;
    border-radius: 50%;
    background: radial-gradient(ellipse at center, var(--ribbon-tint) 0%, var(--ribbon-fade) 70%);
  }
  .brand-name {
    position: absolute;
    left: 66px;
    top: 88px;
    margin: 0;
    font-family: "Poppins", "Century Gothic", sans-serif;
    font-style: italic;
    font-weight: 400;
    font-size: 88px;
    line-height: 1;
    letter-spacing: 1px;
    color: var(--brand-orange);
    -webkit-text-stroke: 3px var(--brand-outline);
    paint-order: stroke fill;
    white-space: nowrap;
  }
  .line {
    position: absolute;
    margin: 0;
    font-size: 34px;
    line-height: 1;
    white-space: nowrap;
  }
  .person-name  { left: 92px;  top: 324px; font-size: 44px; color: var(--name-blue); }
  .person-email { left: 110px; top: 386px; }
  .address      { position: absolute; left: 124px; top: 466px; margin: 0; font-size: 34px; line-height: 42px; font-style: italic; }
  .address span { display: block; }
  .address span:nth-child(1) { padding-left: 8px; }
  .address span:nth-child(2) { padding-left: 4px; }
  .phones       { position: absolute; right: 56px; top: 310px; margin: 0; font-size: 34px; line-height: 42px; text-align: right; }
  .phones span  { display: block; }
  .web-line     { left: 506px; top: 682px; }
  .blog-line    { left: 478px; top: 742px; }
  .social-line  { left: 568px; top: 782px; }
</style>
</head>
<body>
  <main class="card">
    <div class="path-ribbon" role="img" aria-label="Decorative winding ribbon path flowing down the card"></div>

    <h1 class="brand-name">Sunny Paths and joy</h1>

    <p class="line person-name">Leandro T. Ocampo</p>
    <p class="line person-email">leandro@sunnypathsjoy.example</p>

    <address class="address">
      <span>Alameda 482, 3 piso</span>
      <span>Col. Tlalpizco</span>
      <span>Mexico, D.F. 07320</span>
    </address>

    <p class="phones">
      <span>office: (55) 5000-0142</span>
      <span>mobile: (55) 9000-0187</span>
    </p>

    <p class="line web-line">www.sunnypathsjoy.example @sunnypjoy</p>
    <p class="line blog-line">blog: sunnypathsandjoy.blogsite.example</p>
    <p class="line social-line">facebook: SunnyPathsAndJoy</p>

    <div class="card__frame"></div>
  </main>
</body>
</html>
```